Redesign for existing homepage

We would like a redesign for our websites 2 column homepage
We provide engine repair and reconditioning services
We would like a cleaner, modern site that works well with our logo colors
Please see the attached brief for more info
Target Market(s)
25 - 45
Industry/Entity Type
Cleaner
Requirements
Must have
- Google Fonts

```html
<!DOCTYPE html>
<html lang="en">
<head>
<meta charset="utf-8">
<title>Hartwell Engine Works – Specialist Engine Repair &amp; Reconditioning</title>
<link href="https://fonts.googleapis.com/css2?family=Montserrat:wght@500;600;700&family=Open+Sans:wght@400;600;700&display=swap" rel="stylesheet">
<style>
:root{
  --black:#000;
  --blue:#0a5fe0;
  --blue-deep:#0c3fa8;
  --yellow:#ffd200;
  --white:#fff;
  --text:#2b2b2b;
  --grey-link:#d6d6d6;
}
*{margin:0;padding:0;box-sizing:border-box}
html,body{width:1200px;height:1195px;overflow:hidden;background:var(--white)}
body{position:relative;font-family:"Open Sans",Arial,sans-serif;color:var(--text)}
.hero{position:absolute;left:0;top:0;width:1200px;height:806px;
  background:linear-gradient(100deg,#1d3d72 0%,#2f5f9c 30%,#6d89a8 55%,#9aa6b0 75%,#c9cfd3 100%)}
.header-band{position:absolute;left:0;top:0;width:1200px;height:152px}
.nav{position:absolute;top:28px;font-family:"Montserrat",sans-serif;font-weight:600;font-size:17px;color:var(--white);display:flex;gap:30px}
.nav a{color:inherit;text-decoration:none}
.nav-left{left:29px}
.nav-right{right:37px}
.brand{position:absolute;left:0;width:1200px;top:62px;display:flex;justify-content:center;align-items:center;gap:10px;
  font-family:"Montserrat",sans-serif;font-weight:700;font-size:28px;color:var(--yellow)}
.brand-dot{width:22px;height:22px;border-radius:50%;background:var(--blue)}
.headline{position:absolute;left:578px;top:174px;white-space:nowrap;font-family:"Montserrat",sans-serif;font-weight:700;font-size:40px;line-height:52px;color:var(--yellow);text-transform:uppercase;text-shadow:0 2px 4px rgba(0,0,0,.35)}
.subline{position:absolute;left:578px;top:279px;white-space:nowrap;font-family:"Montserrat",sans-serif;font-weight:600;font-size:22px;line-height:27px;color:var(--white);text-transform:uppercase;text-shadow:0 2px 3px rgba(0,0,0,.4)}
.cta{position:absolute;left:578px;top:323px;width:238px;height:55px;background:var(--blue);color:var(--white);font-weight:600;font-size:22px;display:flex;align-items:center;justify-content:center}
.services{position:absolute;left:12px;top:694px;width:1176px;height:332px;background:var(--white);border-radius:10px 10px 0 0}
.service{position:absolute;top:0;width:290px;text-align:center}
.service-photo{position:absolute;top:-70px;width:228px;height:228px;border-radius:50%;border:4px solid var(--white);box-shadow:0 2px 6px rgba(0,0,0,.2)}
.service-title{position:absolute;top:175px;left:0;width:100%;font-weight:700;font-size:17px;color:#111;text-transform:uppercase}
.service-text{position:absolute;top:212px;left:28px;width:240px;text-align:left;font-size:16.5px;line-height:20px;color:#333}
.callbar{position:absolute;left:0;top:1026px;width:1200px;height:88px;background:var(--blue)}
.callbar-text{position:absolute;left:38px;top:30px;font-weight:700;font-size:22px;color:var(--white)}
.callbar-phone{position:absolute;left:599px;top:30px;font-weight:700;font-size:22px;color:var(--yellow)}
.badge{position:absolute}
.badge-a{left:984px;top:1048px;width:50px;height:58px;background:var(--yellow)}
.badge-b{left:1054px;top:1048px;width:108px;height:58px;background:#111;border:1px solid #555}
.footer{position:absolute;left:0;top:1114px;width:1200px;height:81px;background:var(--black)}
.footer-links{position:absolute;left:31px;top:40px;display:flex;gap:15px;font-family:Arial,sans-serif;font-size:13px;color:var(--grey-link)}
.footer-links a{color:inherit;text-decoration:none}
.copyright{position:absolute;right:28px;top:36px;font-family:Arial,sans-serif;font-size:13px;color:var(--grey-link)}
</style>
</head>
<body>
<div class="hero" role="img" aria-label="Mechanic in blue overalls working on a carburettor engine in a workshop"></div>

<svg class="header-band" viewBox="0 0 1200 152" aria-hidden="true">
  <path d="M0 0H1200V76C1020 72 820 150 600 150C380 150 180 72 0 76Z" fill="#000"/>
</svg>

<nav class="nav nav-left"><a href="#">About Us</a><a href="#">Service &amp; Repair</a><a href="#">Trade Customers</a></nav>
<nav class="nav nav-right"><a href="#">Race &amp; Classic Car Engines</a><a href="#">Enquiry</a><a href="#">Contact</a></nav>
<div class="brand"><span class="brand-dot"></span>Hartwell Engine Works</div>

<h1 class="headline">Specialist Engine<br>Repair &amp; Reconditioning</h1>
<p class="subline">To have your car running at its best</p>
<a class="cta">Make an Enquiry</a>

<section class="services">
  <div class="service" style="left:13px">
    <div class="service-photo" role="img" aria-label="Man checking under the bonnet of a family car" style="left:27px;background:linear-gradient(135deg,#7a5a4a,#3a3f4a 60%,#c8ccd2)"></div>
    <h2 class="service-title">Personal Car</h2>
    <p class="service-text">Do you have a personal or family car that needs a repair?</p>
  </div>
  <div class="service" style="left:306px">
    <div class="service-photo" role="img" aria-label="Chrome classic V8 engine with orange air cleaner" style="left:27px;background:radial-gradient(circle at 50% 35%,#c8742a,#3d3d44 55%,#9aa0a8)"></div>
    <h2 class="service-title">Classic Car Engine</h2>
    <p class="service-text">Have a classic car that needs specialist engine work?</p>
  </div>
  <div class="service" style="left:598px">
    <div class="service-photo" role="img" aria-label="Race engine with purple intake components" style="left:27px;background:radial-gradient(circle at 50% 50%,#9a2a8a,#55565e 60%,#b9bcc2)"></div>
    <h2 class="service-title">Race Car Engine</h2>
    <p class="service-text">Own a race car that needs specialist engine repairs?</p>
  </div>
  <div class="service" style="left:885px">
    <div class="service-photo" role="img" aria-label="Two mechanics standing in a garage" style="left:27px;background:linear-gradient(180deg,#8a8f96,#2a2e3a 55%,#a03030)"></div>
    <h2 class="service-title">Garage Owner</h2>
    <p class="service-text">Are you a garage owner, needing to outsource an ...</p>
  </div>
</section>

<section class="callbar">
  <p class="callbar-text">Call us to get your engine running perfectly!</p>
  <p class="callbar-phone">Seaview: (04) 555 0192</p>
</section>
<div class="badge badge-a" aria-hidden="true"></div>
<div class="badge badge-b" aria-hidden="true"></div>

<footer class="footer">
  <nav class="footer-links"><a href="#">About Us</a><a href="#">Private Vehicle Service &amp; Repair</a><a href="#">Trade Customers</a><a href="#">Race &amp; Classic Car Engines</a><a href="#">Make an Enquiry</a><a href="#">Contact Us</a></nav>
  <p class="copyright">© Copyright 2014</p>
</footer>
</body>
</html>
```